Transform this table

Please make a 2 page A4 handout from this boring table into an engaging design. The front page can be simple and engaging (a summary of the back where all the detail lives)

Target Market(s)

Business

Requirements
Must have
• Clarity. And impact.
Nice to have
• Icons

```html
<!DOCTYPE html>
<html lang="en">
<head>
<meta charset="utf-8">
<title>Safety Culture Maturity Ladder</title>
<link href="https://fonts.googleapis.com/css2?family=Oswald:wght@400;700&family=Poppins:wght@400;500;600;700&display=swap" rel="stylesheet">
<style>
  :root {
    --stage: #dedede;
    --paper: #ffffff;
    --ink: #1d1d1f;
    --ink-soft: #4a4a4a;
    --navy: #1b2a5c;
    --grid: #ececec;
    --ring: #8a8a8a;
    --red: #c8102e;
    --orange: #ff7a00;
    --yellow: #dccb0a;
    --lime: #7ddc0f;
    --green: #22a31a;
  }
  html, body { margin: 0; padding: 0; }
  body {
    width: 816px; height: 1200px; overflow: hidden;
    background: var(--stage);
    font-family: "Poppins", Arial, sans-serif;
    position: relative;
  }
  .page {
    position: absolute; left: 0; width: 816px; height: 577px;
    background: var(--paper);
    box-shadow: 0 8px 18px rgba(0,0,0,.18);
  }
  .page--summary { top: 12px; }
  .page--detail { top: 611px; }
  .page svg { display: block; width: 816px; height: 577px; }

  .title-main { font-family: "Oswald", "Arial Narrow", sans-serif; font-weight: 700; font-size: 100px; fill: var(--ink); }
  .title-sub { font-family: "Oswald", "Arial Narrow", sans-serif; font-weight: 400; font-size: 100px; fill: #3a3a3a; }
  .trend { font-size: 25px; font-weight: 500; fill: var(--ink); }
  .step-name { font-size: 17px; font-weight: 600; fill: var(--ink); }
  .step-note { font-size: 13px; fill: var(--ink); }
  .badge-label { font-size: 20px; font-weight: 700; fill: #fff; text-anchor: middle; letter-spacing: .3px; }
  .ring { fill: #fff; stroke: var(--ring); stroke-width: 1.6; stroke-dasharray: 6 4; }
  .halo { fill: #fff; filter: url(#soft-shadow); }
  .link { fill: none; stroke: #9a9a9a; stroke-width: 1.6; stroke-dasharray: 6 4; }
  .icon-slot { fill: rgba(255,255,255,.28); }
  .fill-red { fill: var(--red); } .fill-orange { fill: var(--orange); }
  .fill-yellow { fill: var(--yellow); } .fill-lime { fill: var(--lime); }
  .fill-green { fill: var(--green); }

  .item { font-size: 12.2px; fill: var(--ink-soft); }
  .item.strong, .col-head { font-weight: 600; fill: var(--ink); }
  .col-head { font-size: 12.8px; }
  .tagline { font-size: 14px; font-weight: 600; fill: var(--ink); }
  .dot { fill: var(--ink); }
</style>
</head>
<body>

<!-- Front: summary ladder -->
<section class="page page--summary">
<svg viewBox="0 0 1370 968" aria-label="Safety culture maturity ladder summary">
  <defs>
    <pattern id="graph" width="22" height="22" patternUnits="userSpaceOnUse">
      <path d="M22 0H0V22" fill="none" stroke="var(--grid)" stroke-width="1"/>
    </pattern>
    <filter id="soft-shadow" x="-30%" y="-30%" width="160%" height="160%">
      <feDropShadow dx="0" dy="4" stdDeviation="5" flood-color="#000" flood-opacity=".22"/>
    </filter>
  </defs>

  <rect width="1370" height="968" fill="url(#graph)"/>

  <text class="title-main" x="40" y="125" transform="skewX(-8)" dx="14">SAFETY CULTURE</text>
  <text class="title-sub" x="40" y="228" transform="skewX(-8)" dx="30">MATURITY LADDER</text>

  <!-- trend arrow -->
  <line x1="270" y1="543" x2="832" y2="196" stroke="var(--navy)" stroke-width="4"/>
  <path d="M842,190 L818,190 L830,208Z" fill="var(--navy)"/>
  <g transform="translate(550,333) rotate(-31.5)">
    <text class="trend" x="0" y="-8" text-anchor="middle">Improving safety culture</text>
    <text class="trend" x="-10" y="62" text-anchor="middle">Increasing accountability &amp; reliability</text>
  </g>

  <!-- connectors -->
  <g>
    <polyline id="ladder-path" class="link" points="206,801 436,654 672,503 905,356 1138,211" stroke-dasharray="none" stroke="#777"/>
    <use href="#ladder-path" transform="translate(4,-8)"/>
  </g>
  <path d="M1225,105 L1250,90 L1245,80 L1300,98 L1288,148 L1278,138 L1260,148" fill="none" stroke="#777" stroke-width="1.6" stroke-dasharray="6 4"/>

  <!-- badges -->
  <g transform="translate(206,801)">
    <circle class="ring" r="115"/><circle class="halo" r="98"/><circle class="fill-red" r="88"/>
    <circle class="icon-slot" cy="-28" r="32" role="img" aria-label="Icon: shield with tick and gear"/>
    <text class="badge-label" y="42">VULNERABLE</text>
  </g>
  <g transform="translate(436,654)">
    <circle class="ring" r="115"/><circle class="halo" r="98"/><circle class="fill-orange" r="88"/>
    <circle class="icon-slot" cy="-22" r="34" role="img" aria-label="Icon: atom"/>
    <text class="badge-label" y="50">REACTIVE</text>
  </g>
  <g transform="translate(672,503)">
    <circle class="ring" r="115"/><circle class="halo" r="98"/><circle class="fill-yellow" r="88"/>
    <circle class="icon-slot" cy="-28" r="32" role="img" aria-label="Icon: clipboard with tick"/>
    <text class="badge-label" y="42">COMPLIANT</text>
  </g>
  <g transform="translate(905,356)">
    <circle class="ring" r="115"/><circle class="halo" r="98"/><circle class="fill-lime" r="88"/>
    <circle class="icon-slot" cy="-24" r="34" role="img" aria-label="Icon: gear with light bulb"/>
    <text class="badge-label" y="52">PROACTIVE</text>
  </g>
  <g transform="translate(1138,211)">
    <circle class="ring" r="115"/><circle class="halo" r="98"/><circle class="fill-green" r="88"/>
    <circle class="icon-slot" cy="-22" r="34" role="img" aria-label="Icon: arrows converging on lines"/>
    <text class="badge-label" y="50">RESILIENT</text>
  </g>

  <!-- steps -->
  <g class="steps">
    <text class="step-name" x="320" y="898">Toxic / No care culture</text>
    <text class="step-name" x="320" y="918">“accidents happen”</text>

    <path d="M527,886 Q600,886 600,828" fill="none" stroke="var(--navy)" stroke-width="2"/>
    <path d="M592,840 L600,828 L608,840" fill="none" stroke="var(--navy)" stroke-width="2"/>
    <text class="step-note" x="596" y="877">Wake management &amp;</text>
    <text class="step-note" x="596" y="893">control high risks</text>

    <text class="step-name" x="545" y="771">Blame culture</text>
    <text class="step-name" x="545" y="791">“it was an accident!”</text>

    <path d="M687,747 Q760,747 760,688" fill="none" stroke="var(--navy)" stroke-width="2"/>
    <path d="M752,700 L760,688 L768,700" fill="none" stroke="var(--navy)" stroke-width="2"/>
    <text class="step-note" x="759" y="742">Standardise processes &amp;</text>
    <text class="step-note" x="759" y="758">gain commitment</text>

    <text class="step-name" x="743" y="639">Compliance culture</text>
    <text class="step-name" x="743" y="659">“Incidents have causes”</text>

    <path d="M877,603 Q950,603 950,545" fill="none" stroke="var(--navy)" stroke-width="2"/>
    <path d="M942,557 L950,545 L958,557" fill="none" stroke="var(--navy)" stroke-width="2"/>
    <text class="step-note" x="952" y="593">All team members engaged &amp;</text>
    <text class="step-note" x="952" y="609">all risks controlled</text>

    <text class="step-name" x="930" y="495">Ownership culture</text>
    <text class="step-name" x="930" y="515">“We prevent incidents”</text>

    <path d="M1037,459 Q1110,459 1110,400" fill="none" stroke="var(--navy)" stroke-width="2"/>
    <path d="M1102,412 L1110,400 L1118,412" fill="none" stroke="var(--navy)" stroke-width="2"/>
    <text class="step-note" x="1125" y="448">Develop consistency &amp;</text>
    <text class="step-note" x="1125" y="464">fight complacency</text>

    <text class="step-name" x="1104" y="356">Interdependent culture</text>
    <text class="step-name" x="1104" y="376">“It’s how we do business.”</text>
  </g>

  <line x1="800" y1="934" x2="1330" y2="934" stroke="var(--navy)" stroke-width="2"/>
</svg>
</section>

<!-- Back: detail -->
<section class="page page--detail">
<svg viewBox="0 0 1370 968" aria-label="Safety culture maturity ladder detail">
  <defs>
    <filter id="soft-shadow-2" x="-30%" y="-30%" width="160%" height="160%">
      <feDropShadow dx="0" dy="4" stdDeviation="5" flood-color="#000" flood-opacity=".22"/>
    </filter>
  </defs>
  <!-- connectors -->
  <g>
    <polyline id="detail-path" class="link" points="139,687 407,594 681,525 945,454 1237,367"/>
    <use href="#detail-path" transform="translate(2,8)"/>
  </g>
  <path d="M1330,338 L1350,332 L1345,324 L1362,338 L1348,356 L1346,346 L1332,350" fill="none" stroke="#888" stroke-width="1.4" stroke-dasharray="5 3"/>

  <g transform="translate(139,687) scale(.83)">
    <circle class="ring" r="115"/><circle class="halo" r="98"/><circle class="fill-red" r="88"/>
    <circle class="icon-slot" cy="-28" r="32" role="img" aria-label="Icon: shield with tick and gear"/>
    <text class="badge-label" y="42">VULNERABLE</text>
  </g>
  <g transform="translate(407,594) scale(.83)">
    <circle class="ring" r="115"/><circle class="halo" r="98"/><circle class="fill-orange" r="88"/>
    <circle class="icon-slot" cy="-22" r="34" role="img" aria-label="Icon: atom"/>
    <text class="badge-label" y="50">REACTIVE</text>
  </g>
  <g transform="translate(681,525) scale(.83)">
    <circle class="ring" r="115"/><circle class="halo" r="98"/><circle class="fill-yellow" r="88"/>
    <circle class="icon-slot" cy="-28" r="32" role="img" aria-label="Icon: clipboard with tick"/>
    <text class="badge-label" y="42">COMPLIANT</text>
  </g>
  <g transform="translate(945,454) scale(.83)">
    <circle class="ring" r="115"/><circle class="halo" r="98"/><circle class="fill-lime" r="88"/>
    <circle class="icon-slot" cy="-24" r="34" role="img" aria-label="Icon: gear with light bulb"/>
    <text class="badge-label" y="52">PROACTIVE</text>
  </g>
  <g transform="translate(1237,367) scale(.83)">
    <circle class="ring" r="115"/><circle class="halo" r="98"/><circle class="fill-green" r="88"/>
    <circle class="icon-slot" cy="-22" r="34" role="img" aria-label="Icon: arrows converging on lines"/>
    <text class="badge-label" y="50">RESILIENT</text>
  </g>

  <!-- Column 1: Vulnerable -->
  <g class="col col--vulnerable">
    <circle class="fill-red" cx="22" cy="36" r="4"/>
    <text class="col-head" x="32" y="40">Toxic / No care culture</text>
    <g class="dot">
      <circle cx="37" cy="63" r="2"/><circle cx="37" cy="89" r="2"/><circle cx="37" cy="115" r="2"/>
      <circle cx="37" cy="141" r="2"/><circle cx="37" cy="167" r="2"/><circle cx="37" cy="193" r="2"/>
      <circle cx="37" cy="245" r="2"/>
      <circle cx="22" cy="271" r="2"/><circle cx="22" cy="297" r="2"/><circle cx="22" cy="323" r="2"/>
      <circle cx="22" cy="349" r="2"/><circle cx="22" cy="401" r="2"/><circle cx="22" cy="427" r="2"/>
      <circle cx="22" cy="453" r="2"/><circle cx="22" cy="479" r="2"/><circle cx="22" cy="505" r="2"/>
      <circle cx="22" cy="792" r="2"/><circle cx="22" cy="818" r="2"/><circle cx="22" cy="844" r="2"/>
      <circle cx="22" cy="870" r="2"/><circle cx="22" cy="896" r="2"/><circle cx="22" cy="922" r="2"/>
    </g>
    <text class="item" x="43" y="67">Apathy / resistance</text>
    <text class="item" x="43" y="93">Near misses not considered</text>
    <text class="item" x="43" y="119">Negligence</text>
    <text class="item" x="43" y="145">Dishonesty</text>
    <text class="item" x="43" y="171">Hiding of incidents</text>
    <text class="item" x="43" y="197">Serious injury/health risks are</text>
    <text class="item" x="43" y="223">unseen or ignored</text>
    <text class="item" x="43" y="249">Unfair disciplinary actions</text>
    <text class="item" x="32" y="275">No or little training</text>
    <text class="item" x="32" y="301">Poor or no communication</text>
    <text class="item" x="32" y="327">Production at almost any cost</text>
    <text class="item" x="32" y="353">“Just get it done” attitude or</text>
    <text class="item" x="32" y="379">blatantly unsafe</text>
    <text class="item" x="32" y="405">Reactive or unresponsive approach</text>
    <text class="item" x="32" y="431">No OHS systems</text>
    <text class="item" x="32" y="457">No risk assessment</text>
    <text class="item" x="32" y="483">Legal non compliance</text>
    <text class="item" x="32" y="509">Accept equipment / process decay</text>
    <text class="tagline" x="40" y="556">Accept that incidents happen</text>
    <text class="item" x="32" y="796">Only fix when broken / unsafe repairs</text>
    <text class="item" x="32" y="822">Reports are shelved / used irresponsibly</text>
    <text class="item" x="32" y="848">No or poor investigation</text>
    <text class="item" x="32" y="874">No monitoring / audits</text>
    <text class="item" x="32" y="900">Permit non-compliance</text>
    <text class="item" x="32" y="926">Potential illegal practices</text>
  </g>

  <!-- Column 2: Reactive -->
  <g class="col col--reactive">
    <circle class="fill-orange" cx="281" cy="36" r="4"/>
    <text class="col-head" x="296" y="40">Blame culture</text>
    <g class="dot">
      <circle cx="296" cy="62" r="2"/><circle cx="296" cy="88" r="2"/><circle cx="296" cy="114" r="2"/>
      <circle cx="296" cy="140" r="2"/><circle cx="296" cy="192" r="2"/>
      <circle cx="281" cy="218" r="2"/><circle cx="281" cy="244" r="2"/><circle cx="281" cy="296" r="2"/>
      <circle cx="281" cy="322" r="2"/><circle cx="281" cy="374" r="2"/><circle cx="281" cy="400" r="2"/>
      <circle cx="281" cy="426" r="2"/>
      <circle cx="281" cy="712" r="2"/><circle cx="296" cy="738" r="2"/><circle cx="296" cy="764" r="2"/>
      <circle cx="296" cy="790" r="2"/><circle cx="281" cy="816" r="2"/><circle cx="281" cy="842" r="2"/>
      <circle cx="281" cy="894" r="2"/><circle cx="281" cy="920" r="2"/>
    </g>
    <text class="item strong" x="304" y="66">Dependent on natural instincts</text>
    <text class="item" x="304" y="92">Accept need to care</text>
    <text class="item" x="304" y="118">Some near miss reporting</text>
    <text class="item" x="304" y="144">Some window dressing e.g. pre-</text>
    <text class="item" x="304" y="170">inspection cleanups and light duty</text>
    <text class="item" x="304" y="196">Disciplinary action</text>
    <text class="item" x="296" y="222">Minimum / inconsistent training</text>
    <text class="item" x="296" y="248">Some communication on a need to</text>
    <text class="item" x="296" y="274">know basis</text>
    <text class="item" x="296" y="300">Administrator driven</text>
    <text class="item" x="296" y="326">Loose systems, elements of an OHS</text>
    <text class="item" x="296" y="352">Management System</text>
    <text class="item strong" x="296" y="378">Reactive risk assessment and control</text>
    <text class="item" x="296" y="404">Minimum legal compliance</text>
    <text class="item" x="296" y="430">Apply PPE as a way of eliminating exposure</text>
    <text class="tagline" x="310" y="482">Prevent a similar incident</text>
    <text class="item strong" x="296" y="716">Incident investigation but limited analysis</text>
    <text class="item" x="307" y="742">Focus on what happened</text>
    <text class="item" x="307" y="768">No systems focus</text>
    <text class="item" x="307" y="794">Human faults occur</text>
    <text class="item" x="296" y="820">Ad hoc monitoring / audits</text>
    <text class="item" x="296" y="846">No occupational hygiene or health</text>
    <text class="item" x="296" y="872">initiatives</text>
    <text class="item" x="296" y="898">Reactive medical monitoring</text>
    <text class="item" x="296" y="924">Monitoring as per regulations</text>
  </g>

  <!-- Column 3: Compliant -->
  <g class="col col--compliant">
    <circle class="fill-yellow" cx="566" cy="36" r="4"/>
    <text class="col-head" x="578" y="40">Compliance culture</text>
    <g class="dot">
      <circle cx="582" cy="62" r="2"/><circle cx="582" cy="88" r="2"/><circle cx="582" cy="114" r="2"/>
      <circle cx="566" cy="140" r="2"/><circle cx="566" cy="166" r="2"/><circle cx="566" cy="218" r="2"/>
      <circle cx="566" cy="244" r="2"/><circle cx="566" cy="270" r="2"/><circle cx="566" cy="322" r="2"/>
      <circle cx="566" cy="348" r="2"/>
      <circle cx="566" cy="660" r="2"/><circle cx="566" cy="712" r="2"/><circle cx="566" cy="764" r="2"/>
      <circle cx="566" cy="790" r="2"/><circle cx="566" cy="842" r="2"/><circle cx="566" cy="868" r="2"/>
      <circle cx="566" cy="894" r="2"/><circle cx="566" cy="920" r="2"/>
    </g>
    <text class="item strong" x="588" y="66">Supervision dependent</text>
    <text class="item" x="588" y="92">Some participation</text>
    <text class="item" x="588" y="118">Near miss discussions</text>
    <text class="item" x="578" y="144">Acceptable training / awareness</text>
    <text class="item" x="578" y="170">Established and good communication</text>
    <text class="item" x="578" y="196">channels</text>
    <text class="item" x="578" y="222">Regular people involvement and focus</text>
    <text class="item" x="578" y="248">OHS coordinator driven</text>
    <text class="item" x="578" y="274">OHS standards system and ISO 9002 or</text>
    <text class="item" x="578" y="300">equivalent</text>
    <text class="item strong" x="578" y="326">Risk assessment through existing systems</text>
    <text class="item" x="578" y="352">Total legal compliance goal</text>
    <text class="tagline" x="556" y="405">Prevent incidents before they occur</text>
    <text class="item" x="578" y="664">Strictly enforced the use of PPE where</text>
    <text class="item" x="578" y="690">required (knowing risk)</text>
    <text class="item strong" x="578" y="716">Causal incident analysis based on</text>
    <text class="item strong" x="578" y="742">events potential</text>
    <text class="item" x="578" y="768">Info sharing from events</text>
    <text class="item" x="578" y="794">Planned occupational hygiene /</text>
    <text class="item" x="578" y="820">environmental monitoring</text>
    <text class="item" x="578" y="846">Periodical medical examinations</text>
    <text class="item strong" x="578" y="872">Planned monitoring / audits</text>
    <text class="item" x="578" y="898">Safety meetings and talks</text>
    <text class="item" x="578" y="924">Some task observations</text>
  </g>

  <!-- Column 4: Proactive -->
  <g class="col col--proactive">
    <circle class="fill-lime" cx="856" cy="36" r="4"/>
    <text class="col-head" x="870" y="40">Independent &amp; personal ownership</text>
    <text class="col-head" x="870" y="66">culture</text>
    <g class="dot">
      <circle cx="871" cy="88" r="2"/><circle cx="871" cy="114" r="2"/>
      <circle cx="856" cy="140" r="2"/><circle cx="856" cy="166" r="2"/><circle cx="856" cy="218" r="2"/>
      <circle cx="856" cy="244" r="2"/><circle cx="856" cy="270" r="2"/>
      <circle cx="856" cy="608" r="2"/><circle cx="856" cy="634" r="2"/><circle cx="856" cy="660" r="2"/>
      <circle cx="856" cy="712" r="2"/><circle cx="856" cy="738" r="2"/><circle cx="856" cy="764" r="2"/>
      <circle cx="856" cy="816" r="2"/><circle cx="856" cy="842" r="2"/>
    </g>
    <text class="item" x="881" y="92">Involvement at all levels</text>
    <text class="item" x="881" y="118">Near miss involvement</text>
    <text class="item" x="870" y="144">High level of training / awareness</text>
    <text class="item" x="870" y="170">Communication at a high level hiding</text>
    <text class="item" x="870" y="196">nothing</text>
    <text class="item" x="870" y="222">Committed leadership at all levels</text>
    <text class="item" x="870" y="248">Line driven systems improvement</text>
    <text class="item" x="870" y="274">ISO 14001 and ISO 45001</text>
    <text class="tagline" x="867" y="325">Improve the systems</text>
    <text class="item strong" x="870" y="612">Pro-active formal risk management</text>
    <text class="item" x="870" y="638">Beyond legal compliance</text>
    <text class="item" x="870" y="664">Seek to actively engineer out process /</text>
    <text class="item" x="870" y="690">equipment inadequacies</text>
    <text class="item strong" x="870" y="716">Incident learnings shared with all levels</text>
    <text class="item" x="870" y="742">Well designed plans / procedures</text>
    <text class="item strong" x="870" y="768">Focus on adhering to site plans and</text>
    <text class="item strong" x="870" y="794">procedures</text>
    <text class="item" x="870" y="820">Integrated audits</text>
    <text class="item" x="870" y="846">Peer evaluations and discussion</text>
  </g>

  <!-- Column 5: Resilient -->
  <g class="col col--resilient">
    <circle class="fill-green" cx="1125" cy="36" r="4"/>
    <text class="col-head" x="1139" y="40">Interdependent teams culture</text>
    <g class="dot">
      <circle cx="1125" cy="62" r="2"/><circle cx="1140" cy="88" r="2"/><circle cx="1140" cy="114" r="2"/>
      <circle cx="1125" cy="192" r="2"/>
      <circle cx="1125" cy="504" r="2"/><circle cx="1125" cy="530" r="2"/><circle cx="1125" cy="556" r="2"/>
      <circle cx="1125" cy="582" r="2"/><circle cx="1125" cy="634" r="2"/><circle cx="1125" cy="660" r="2"/>
      <circle cx="1125" cy="686" r="2"/><circle cx="1125" cy="738" r="2"/><circle cx="1125" cy="764" r="2"/>
      <circle cx="1125" cy="816" r="2"/><circle cx="1125" cy="868" r="2"/><circle cx="1125" cy="920" r="2"/>
    </g>
    <text class="item" x="1139" y="66">Way of life</text>
    <text class="item" x="1150" y="92">Comes natural</text>
    <text class="item" x="1150" y="118">Personal involvement by all to</text>
    <text class="item" x="1150" y="144">manage risks well and prevent</text>
    <text class="item" x="1150" y="170">incidents</text>
    <text class="item" x="1139" y="196">Authentic communication</text>
    <text class="item" x="1139" y="222">throughout culture</text>
    <text class="tagline" x="1171" y="259">Way we do business</text>
    <text class="item" x="1139" y="508">Individually internalized</text>
    <text class="item" x="1139" y="534">Inspiring genuine leadership</text>
    <text class="item" x="1139" y="560">No silo thinking or actions</text>
    <text class="item" x="1139" y="586">All staff active, positive, respected,</text>
    <text class="item" x="1139" y="612">speaking up</text>
    <text class="item" x="1139" y="638">Excellent equipment, ultra-organised</text>
    <text class="item" x="1139" y="664">Integrated management systems</text>
    <text class="item strong" x="1139" y="690">Risk management cycle integrated</text>
    <text class="item strong" x="1139" y="716">into all systems</text>
    <text class="item" x="1139" y="742">Self regulating style</text>
    <text class="item" x="1139" y="768">Eliminate &amp; prevent problems before</text>
    <text class="item" x="1139" y="794">they occur</text>
    <text class="item" x="1139" y="820">All threats considered in decision-</text>
    <text class="item" x="1139" y="846">making</text>
    <text class="item strong" x="1139" y="872">Continually improving through</text>
    <text class="item strong" x="1139" y="898">external evaluation / auditing</text>
    <text class="item" x="1139" y="924">Multiple positive performance</text>
    <text class="item" x="1139" y="950">indicators drive PDCA cycle</text>
  </g>
</svg>
</section>

</body>
</html>
```